VELTRIX Web Page

We need a corporate web site for a new company VELTRIX Corporation. VELTRIX is a technology company that has developed a new virtualization solution for corporate applications. Our target customers are IT professionals. We have a logo, which we will provide.

Final design should communicate: innovation, stability, professionalism

Industry/Entity Type

It Company

```html
<!DOCTYPE html>
<html lang="en">
<head>
<meta charset="utf-8">
<title>VELTRIX Corporation</title>
<link href="https://fonts.googleapis.com/css2?family=Oswald:wght@300&family=PT+Sans:wght@400;700&family=Arimo:ital,wght@0,400;1,400&display=swap" rel="stylesheet">
<style>
:root{
  --page:#f4f4f4;
  --ink:#4a4a4a;
  --muted:#6f6f6f;
  --line:#d9d9d9;
  --blue:#9cc3d9;
  --mint:#98d3bd;
  --lime:#c3d97a;
  --rose:#d49fa0;
  --card:#e9e9e9;
  --link:#2aa1dd;
  --footer:#e6e6e6;
}
*{margin:0;padding:0;box-sizing:border-box}
html,body{width:1200px;height:1136px;overflow:hidden}
body{background:var(--page);font-family:"Arimo",Arial,sans-serif;color:var(--ink);position:relative}
.abs{position:absolute}
.site-header{position:absolute;left:0;top:0;width:1200px;height:86px;background:#f1f1f1}
.header-rule{position:absolute;left:0;top:86px;width:1200px;height:8px;background:var(--line)}
.logo{left:194px;top:20px;font-family:"Oswald",sans-serif;font-weight:300;font-size:28px;color:#555;letter-spacing:.2px}
.nav a{position:absolute;top:40px;font-size:14px;color:#555;text-decoration:none;transform:translateX(-50%)}
.nav .home{left:454px;top:32px;width:85px;height:35px;background:var(--blue);color:#fff;border-radius:4px;transform:skewY(1deg);display:flex;align-items:center;justify-content:center;font-size:14px}
.hero-bg{left:0;top:94px;width:1200px;height:362px;background:linear-gradient(180deg,#ececec 0%,#f6f6f6 80%,var(--page) 100%)}
.hero-photo{left:193px;top:94px;width:813px;height:362px;background:linear-gradient(90deg,#f2f2f2 0%,#e3e9ee 30%,#b9c7cf 55%,#6d6f73 75%,#c8b7a8 100%)}
.hero-fade{left:0;top:380px;width:1200px;height:80px;background:linear-gradient(180deg,rgba(244,244,244,0),var(--page))}
.hero-title{left:193px;top:188px;font-family:"PT Sans",sans-serif;font-size:36px;line-height:43px;color:#555;letter-spacing:.5px}
.hero-text{left:193px;top:283px;width:370px;font-family:"PT Sans",sans-serif;font-size:12.5px;line-height:19px;color:#555}
.dots{left:193px;top:389px;display:flex;gap:5px}
.dots span{width:14px;height:14px;border:2px solid #c4c4c4;border-radius:50%}
.dots span.on{border-color:var(--blue)}
.card{position:absolute;top:485px;width:193px;height:243px}
.card svg{position:absolute;left:0;top:0}
.card h3{position:absolute;left:17px;top:11px;font-weight:400;font-size:20px;color:#fff}
.card p{position:absolute;left:17px;top:92px;width:160px;font-size:12px;line-height:17.2px;color:#8a8a8a}
.card .more{position:absolute;left:131px;top:201px;width:45px;height:25px;border-radius:4px;color:#fff;font-style:italic;font-size:12px;display:flex;align-items:center;justify-content:center}
.section-title{font-weight:400;color:#555}
.solutions-title{left:193px;top:750px;font-size:25px}
.portrait{left:193px;top:795px;width:172px;height:160px;border:1px solid #ddd;background:#fff;padding:3px}
.portrait div{width:100%;height:100%;background:linear-gradient(180deg,#f6f6f6,#e4e4e4 70%,#cfcfcf)}
.solutions-text{left:383px;top:797px;width:300px;font-size:12.5px;line-height:17.2px;color:#555}
.solutions-text p+p{margin-top:17px}
.btn{position:absolute;background:var(--blue);color:#fff;font-style:italic;font-size:12.5px;border-radius:4px;display:flex;align-items:center;justify-content:center}
.offer-title{left:707px;top:750px;font-size:21px}
.offer{position:absolute;left:707px;width:300px}
.offer .thumb{position:absolute;left:0;top:0;width:78px;height:78px;border:1px solid #ddd;background:#fff;padding:2px}
.offer .thumb div{width:100%;height:100%}
.offer h4{position:absolute;left:95px;top:0;font-weight:400;font-size:14px;color:var(--link)}
.offer p{position:absolute;left:95px;top:25px;width:205px;font-size:12.5px;line-height:17.2px;color:#555}
.site-footer{left:0;top:1036px;width:1200px;height:100px;background:var(--footer)}
.copy{left:193px;top:1072px;font-size:14px;color:#555}
.copy-line{left:193px;top:1093px;font-size:10.5px;color:#666}
.follow{left:882px;top:1060px;font-size:14px;color:#555}
.social{left:882px;top:1088px;display:flex;gap:9px}
.social span{width:24px;height:24px;background:#c9c9c9}
</style>
</head>
<body>
<header class="site-header">
  <div class="abs logo">VELTRIX Corporation</div>
  <nav class="nav">
    <a class="home" href="#">Home</a>
    <a href="#" style="left:589px">Company</a>
    <a href="#" style="left:683px">Services</a>
    <a href="#" style="left:776px">Careers</a>
    <a href="#" style="left:870px">Clients</a>
    <a href="#" style="left:963px">Contacts</a>
  </nav>
</header>
<div class="header-rule"></div>

<section>
  <div class="abs hero-bg"></div>
  <div class="abs hero-photo" role="img" aria-label="Photo of three business colleagues in an office, a smiling woman in the foreground"></div>
  <div class="abs" style="left:193px;top:94px;width:420px;height:362px;background:linear-gradient(90deg,rgba(244,244,244,.9),rgba(244,244,244,0))"></div>
  <div class="abs hero-fade"></div>
  <h1 class="abs hero-title" style="font-weight:400">Lorem ipsum dolor<br>sit amet</h1>
  <p class="abs hero-text">Lorem ipsum dolor sit amet, consectetur adipiscing elit. Sed eget est neque. Nulla at arcu lectus, sed trum tellus Nam accumsan, nisi sed pharetra mattis</p>
  <div class="abs dots"><span class="on"></span><span></span><span></span><span></span></div>
</section>

<section>
  <div class="card" style="left:193px">
    <svg width="193" height="243" viewBox="0 0 193 243"><path d="M7,6 Q7,0 13,0 L179,9 Q186,10 186,17 L189,130 L7,130 Z" fill="var(--blue)"/><path d="M0,57 Q0,51 6,50 L165,33 Q173,32 174,40 L193,236 Q193,243 186,243 L6,243 Q0,243 0,237 Z" fill="var(--card)"/><path d="M146,47 h22 q4,0 4,4 v10 q0,4 -4,4 h-15 l-6,5 v-5 q-5,0 -5,-4 v-10 q0,-4 4,-4z" fill="#8a8a8a"/><g fill="#e9e9e9"><circle cx="153" cy="57" r="1.4"/><circle cx="158" cy="57" r="1.4"/><circle cx="163" cy="57" r="1.4"/></g></svg>
    <h3>Support</h3>
    <p>Natoqe penatus magnis par-turient montes diculus nulla duim fusegin alesda odio morb nuncodio. gravida cursus necluctus lorenas tristique acem auctor...</p>
    <span class="more" style="background:var(--blue)">More</span>
  </div>
  <div class="card" style="left:400px">
    <svg width="193" height="243" viewBox="0 0 193 243"><path d="M7,6 Q7,0 13,0 L179,9 Q186,10 186,17 L189,130 L7,130 Z" fill="var(--mint)"/><path d="M0,57 Q0,51 6,50 L165,33 Q173,32 174,40 L193,236 Q193,243 186,243 L6,243 Q0,243 0,237 Z" fill="var(--card)"/><path d="M146,69 Q142,50 172,45 Q170,70 146,69z" fill="#8a8a8a"/><path d="M144,71 L166,51" stroke="#e9e9e9" stroke-width="1.5"/></svg>
    <h3>Analysis</h3>
    <p>Natoqe penatus magnis par-turient montes diculus nulla duim fusegin alesda odio morb nuncodio. gravida cursus necluctus lorenas tristique acem auctor...</p>
    <span class="more" style="background:var(--mint)">More</span>
  </div>
  <div class="card" style="left:607px">
    <svg width="193" height="243" viewBox="0 0 193 243"><path d="M7,6 Q7,0 13,0 L179,9 Q186,10 186,17 L189,130 L7,130 Z" fill="var(--lime)"/><path d="M0,57 Q0,51 6,50 L165,33 Q173,32 174,40 L193,236 Q193,243 186,243 L6,243 Q0,243 0,237 Z" fill="var(--card)"/><circle cx="159" cy="57" r="13" fill="#8a8a8a"/><path d="M150,50 q6,2 5,7 q-3,4 0,9 M162,46 q-2,6 4,8 q4,1 5,6" stroke="#e9e9e9" stroke-width="2" fill="none"/></svg>
    <h3>Experience</h3>
    <p>Natoqe penatus magnis par-turient montes diculus nulla duim fusegin alesda odio morb nuncodio. gravida cursus necluctus lorenas tristique acem auctor...</p>
    <span class="more" style="background:var(--lime)">More</span>
  </div>
  <div class="card" style="left:814px">
    <svg width="193" height="243" viewBox="0 0 193 243"><path d="M7,6 Q7,0 13,0 L179,9 Q186,10 186,17 L189,130 L7,130 Z" fill="var(--rose)"/><path d="M0,57 Q0,51 6,50 L165,33 Q173,32 174,40 L193,236 Q193,243 186,243 L6,243 Q0,243 0,237 Z" fill="var(--card)"/><circle cx="158" cy="57" r="13" fill="#8a8a8a"/><path d="M161,45 L153,59 L159,59 L155,69" stroke="#e9e9e9" stroke-width="2.5" fill="none"/></svg>
    <h3>Strategies</h3>
    <p>Natoqe penatus magnis par-turient montes diculus nulla duim fusegin alesda odio morb nuncodio. gravida cursus necluctus lorenas tristique acem auctor...</p>
    <span class="more" style="background:var(--rose)">More</span>
  </div>
</section>

<section>
  <h2 class="abs section-title solutions-title">Best Solutions for Growing Business</h2>
  <div class="abs portrait"><div role="img" aria-label="Photo of a smiling young man giving a thumbs up"></div></div>
  <div class="abs solutions-text">
    <p>Magnis parturient montes diculus nulla fusegin alesda odio morb nuncodio. gravida cursus necluctus lorenas tristique acem auctor ultricies.</p>
    <p>Donec accumsan malesuada orci. Donec situmamet eros. Lorem ipsum dolor consecetuer adipiscing mauris fermentum dictum magna. Sed laoreet aliquam leo. Utellus dolor, dapibus eget, elementum velcursus eleif aenean auctor aliquam erat volutpat.</p>
  </div>
  <a class="btn" style="left:382px;top:972px;width:78px;height:28px">Read More</a>
</section>

<section>
  <h2 class="abs section-title offer-title">What We Offer</h2>
  <div class="offer" style="top:792px">
    <div class="thumb"><div role="img" aria-label="Photo of a man talking on a phone" style="background:linear-gradient(180deg,#dfe6ec,#9fb3c4)"></div></div>
    <h4>Consulting Services</h4>
    <p>Accusamu dolore massa fugharum quidemed rerum facilis iusto ssimos ducimus eos et ...</p>
  </div>
  <div class="offer" style="top:887px">
    <div class="thumb"><div role="img" aria-label="Photo of a smiling blonde woman" style="background:linear-gradient(180deg,#eef0f0,#d8c7b0)"></div></div>
    <h4>Regulatory Support</h4>
    <p>Accusamu dolore massa fugharum quidemed rerum facilis iusto ssimos ducimus eos et ...</p>
  </div>
  <a class="btn" style="left:707px;top:982px;width:78px;height:28px">View All</a>
</section>

<footer class="abs site-footer">
</footer>
<div class="abs copy">Copyright</div>
<div class="abs copy-line">Veltrix Corporation 2013 | PRIVACY POLICY</div>
<div class="abs follow">FOLLOW US ON</div>
<div class="abs social"><span></span><span></span><span></span><span></span></div>
</body>
</html>
```